Book for children

We're looking for very nice, creative and well crafted set of graphics to animate an interactive children's book Lumo app that teaches children the hebrew alphabet.

This involves creating a theme and bringing in to live with the letters, creating a set of frame images for animating each letter around the selected theme

We are willing to work hand to hand with designers to achieve the best result and will provide:
- All the Hebrew Alphabet letters.
- Instructions for frame sizes and needs
- Time period may be extended

We have many other projects in case a successful partnership evolves

Reason: - Need a few more days to decide

Target Market(s)

children 2.5 - 4

Industry/Entity Type

Work

Requirements
Must have
• the project requires graphics and animations for each scene
. background designs for each letter
. animations for each letter, we need a good quantity of frames to animate the letters.
. the design should be around a selected theme ex: animals, in this case each letter should represent an animal, matching the animal name and the letter.

```html
<!DOCTYPE html>
<html lang="en">
<head>
<meta charset="utf-8">
<title>Lumo Alphabet – Hay</title>
<link rel="stylesheet" href="https://fonts.googleapis.com/css2?family=Secular+One&family=Cabin+Sketch:wght@700&family=Gochi+Hand&display=swap">
<style>
  :root {
    --stage-orange: #f05a2a;
    --frame-tan: #c9a66b;
    --frame-tan-light: #dcbf8a;
    --board-dark: #232323;
    --chalk-white: #ffffff;
    --glow: rgba(255, 240, 170, 0.85);
    --button-dark: #1a1a1a;
    --zebra-tone: #3a3a3a;
  }
  * { margin: 0; padding: 0; box-sizing: border-box; }
  html, body {
    width: 1200px; height: 1000px; overflow: hidden;
    background: var(--stage-orange);
  }
  .app-screen {
    position: relative; width: 1200px; height: 1000px;
    background: var(--stage-orange);
  }
  .board-frame {
    position: absolute; left: 26px; top: 161px; width: 1152px; height: 665px;
    background: linear-gradient(180deg, var(--frame-tan-light), var(--frame-tan));
    transform: rotate(-0.6deg);
    box-shadow: 0 2px 6px rgba(0,0,0,0.25);
  }
  .chalkboard {
    position: absolute; left: 44px; top: 25px; width: 1069px; height: 615px;
    background: var(--board-dark);
    color: var(--chalk-white);
  }
  .menu-icons {
    position: absolute; left: 26px; top: 21px; display: flex; gap: 26px; align-items: center;
  }
  .animal-illustration {
    position: absolute; left: 141px; top: 52px; width: 360px; height: 416px;
    background: radial-gradient(ellipse at 50% 45%, #5a5a5a 0%, var(--zebra-tone) 60%, var(--board-dark) 100%);
    border-radius: 24px;
  }
  .nav-button {
    position: absolute; top: 275px; width: 76px; height: 76px; border-radius: 50%;
    background: var(--button-dark);
    display: flex; align-items: center; justify-content: center;
  }
  .nav-prev { left: 37px; }
  .nav-next { left: 959px; }
  .hebrew-letter {
    position: absolute; left: 660px; top: 30px; width: 230px;
    font-family: "Secular One", sans-serif; font-size: 330px; line-height: 1;
    text-align: center; color: var(--chalk-white);
    text-shadow: 0 0 10px var(--glow), 0 0 22px var(--glow);
  }
  .letter-name {
    position: absolute; left: 645px; top: 388px; width: 250px;
    font-family: "Cabin Sketch", cursive; font-weight: 700; font-size: 128px;
    line-height: 1; text-align: center; letter-spacing: 2px;
  }
  .tap-hint {
    position: absolute; left: 909px; top: 94px;
    font-family: "Gochi Hand", cursive; font-size: 17px; line-height: 1.15;
  }
  .hint-arrow { position: absolute; left: 882px; top: 138px; }
  .info-button { position: absolute; left: 1024px; top: 556px; }
  .vowel-mark {
    position: absolute; left: 730px; top: 596px; width: 128px; height: 13px;
    background: var(--chalk-white); transform: rotate(3deg);
  }
</style>
</head>
<body>
<main class="app-screen">
  <section class="board-frame">
    <div class="chalkboard">
      <nav class="menu-icons">
        <svg class="grid-icon" width="38" height="38" viewBox="0 0 38 38" aria-label="All letters">
          <g fill="#fff">
            <rect x="0" y="0" width="10" height="10"/><rect x="14" y="0" width="10" height="10"/><rect x="28" y="0" width="10" height="10"/>
            <rect x="0" y="14" width="10" height="10"/><rect x="14" y="14" width="10" height="10"/><rect x="28" y="14" width="10" height="10"/>
            <rect x="0" y="28" width="10" height="10"/><rect x="14" y="28" width="10" height="10"/><rect x="28" y="28" width="10" height="10"/>
          </g>
        </svg>
        <svg class="replay-icon" width="36" height="36" viewBox="0 0 36 36" aria-label="Replay">
          <path d="M28 12 A13 13 0 1 0 31 20" fill="none" stroke="#fff" stroke-width="3.5" stroke-linecap="round"/>
          <path d="M22 10 L30 11 L30 3" fill="none" stroke="#fff" stroke-width="3.5" stroke-linecap="round" stroke-linejoin="round"/>
        </svg>
      </nav>

      <div class="animal-illustration" role="img" aria-label="Chalk drawing of a zebra whose striped body forms the letter Hay"></div>

      <a class="nav-button nav-prev" aria-label="Previous letter">
        <svg width="24" height="30" viewBox="0 0 24 30"><path d="M18 4 L6 15 L18 26" fill="none" stroke="#fff" stroke-width="3.5" stroke-linecap="round" stroke-linejoin="round"/></svg>
      </a>
      <a class="nav-button nav-next" aria-label="Next letter">
        <svg width="24" height="30" viewBox="0 0 24 30"><path d="M6 4 L18 15 L6 26" fill="none" stroke="#fff" stroke-width="3.5" stroke-linecap="round" stroke-linejoin="round"/></svg>
      </a>

      <div class="hebrew-letter" lang="he">ה</div>
      <div class="letter-name">HAY</div>

      <p class="tap-hint">tap the letter<br>to hear it</p>
      <svg class="hint-arrow" width="80" height="50" viewBox="0 0 80 50" aria-hidden="true">
        <path d="M4 44 C30 44 52 34 62 10" fill="none" stroke="#fff" stroke-width="2" stroke-linecap="round"/>
        <path d="M55 14 L62 8 L66 17" fill="none" stroke="#fff" stroke-width="2" stroke-linecap="round" stroke-linejoin="round"/>
      </svg>

      <svg class="info-button" width="26" height="26" viewBox="0 0 26 26" aria-label="Info">
        <circle cx="13" cy="13" r="12" fill="#fff"/>
        <rect x="11.3" y="11" width="3.4" height="9" fill="#232323"/>
        <circle cx="13" cy="7.3" r="2" fill="#232323"/>
      </svg>

      <div class="vowel-mark" aria-hidden="true"></div>
    </div>
  </section>
</main>
</body>
</html>
```